International Trading Company, 'KIRO' needs a Business Card

The company name is "KIRO" and it has own logo design.
I'd like to use its logo on this business card.
I need two side Business Card.
I'll look forward to your great design.
Thank you very much in advance.

Contact Information for Business Card

Company Name : Kiro Harbour Limited
Information Example
Dorian Pallister
Mobile(use icon please) : 1 (212) 555-0143
Tel(use icon please) : 1 (212) 555-0178
Email(use icon please) : dorian27@kiroharbour-mail.com
Address(use icon please) : 482 Halden Ave, New York, NY 10160, USA

```html
<!DOCTYPE html>
<html lang="en">
<head>
<meta charset="utf-8">
<title>Kiro Harbour Limited — Business Card</title>
<link rel="stylesheet" href="https://fonts.googleapis.com/css2?family=Roboto:wght@400;700;900&family=Roboto+Condensed:wght@500&display=swap">
<style>
  :root {
    --backdrop: #2b2b2b;
    --card-dark: #58585a;
    --card-light: #f3f3f3;
    --accent-stripe: #9a9a9a;
    --ink-dark: #545456;
    --ink-light: #ffffff;
  }
  html, body {
    margin: 0;
    padding: 0;
    width: 1200px;
    height: 960px;
    overflow: hidden;
    background: var(--backdrop);
    font-family: "Roboto", Arial, sans-serif;
  }
  .canvas {
    position: relative;
    width: 1200px;
    height: 960px;
  }
  .card {
    position: absolute;
    width: 600px;
    height: 343px;
    overflow: hidden;
    box-shadow: 0 3px 8px rgba(0,0,0,0.5);
  }
  .card--front { left: 314px; top: 113px; background: var(--card-light); }
  .card--back  { left: 311px; top: 472px; background: var(--card-dark); }

  .front-panel {
    position: absolute;
    inset: 0;
  }
  .wordmark {
    position: absolute;
    font-family: "Roboto", Arial, sans-serif;
    font-weight: 900;
    letter-spacing: 0.02em;
    line-height: 1;
    margin: 0;
  }
  .wordmark--front {
    right: 44px;
    top: 42px;
    font-size: 64px;
    color: var(--ink-dark);
  }
  .identity {
    position: absolute;
    left: 38px;
    top: 130px;
    color: var(--ink-light);
  }
  .identity__name {
    font-family: "Roboto Condensed", Arial, sans-serif;
    font-weight: 500;
    font-size: 21px;
    margin: 0;
    letter-spacing: 0.01em;
  }
  .identity__role {
    font-family: "Roboto Condensed", Arial, sans-serif;
    font-weight: 500;
    font-size: 15px;
    margin: 4px 0 0;
  }
  .contact-list {
    position: absolute;
    left: 38px;
    top: 188px;
    margin: 0;
    padding: 0;
    list-style: none;
    color: var(--ink-light);
    font-size: 14.5px;
    line-height: 19px;
  }
  .contact-list li {
    display: flex;
    align-items: flex-start;
  }
  .contact-list .contact--address { margin-bottom: 10px; }
  .contact-icon {
    width: 14px;
    height: 14px;
    margin: 3px 9px 0 0;
    flex: none;
    fill: var(--ink-light);
  }
  .wordmark--back {
    left: 0;
    right: 0;
    top: 133px;
    text-align: center;
    font-size: 90px;
    color: var(--ink-light);
  }
  .back-url {
    position: absolute;
    left: 0;
    right: 0;
    top: 288px;
    text-align: center;
    color: var(--ink-light);
    font-size: 14px;
    letter-spacing: 0.55em;
    margin: 0;
  }
</style>
</head>
<body>
<main class="canvas">
  <section class="card card--front" aria-label="Business card front">
    <svg class="front-panel" width="600" height="343" viewBox="0 0 600 343" aria-hidden="true">
      <polygon points="0,0 149,0 436,343 0,343" fill="var(--card-dark)"/>
      <polygon points="153,0 157,0 447,343 441,343" fill="var(--accent-stripe)"/>
    </svg>
    <p class="wordmark wordmark--front">KIRO</p>
    <div class="identity">
      <h1 class="identity__name">DORIAN PALLISTER</h1>
      <p class="identity__role">CEO/FOUNDER</p>
    </div>
    <ul class="contact-list">
      <li class="contact--address">
        <svg class="contact-icon" viewBox="0 0 14 14" aria-hidden="true"><path d="M7 0.5a4.5 4.5 0 0 0-4.5 4.5c0 3.4 4.5 8.5 4.5 8.5s4.5-5.1 4.5-8.5A4.5 4.5 0 0 0 7 0.5zm0 6.3a1.8 1.8 0 1 1 0-3.6 1.8 1.8 0 0 1 0 3.6z"/></svg>
        <span>482 Halden Ave, New York<br>NY 10160, USA</span>
      </li>
      <li>
        <svg class="contact-icon" viewBox="0 0 14 14" aria-hidden="true"><path d="M3 1l2.2 0.3 1 3-1.5 1.2a8 8 0 0 0 3.8 3.8l1.2-1.5 3 1L13 11c0 1.2-1 2-2 2C5.5 13 1 8.5 1 3c0-1 0.8-2 2-2z"/></svg>
        <span>1 (212) 555-0178</span>
      </li>
      <li>
        <svg class="contact-icon" viewBox="0 0 14 14" aria-hidden="true"><path d="M3.5 0.5h7a1 1 0 0 1 1 1v11a1 1 0 0 1-1 1h-7a1 1 0 0 1-1-1v-11a1 1 0 0 1 1-1zm0.8 1.6v8.6h5.4V2.1zM7 11.3a0.8 0.8 0 1 0 0 1.6 0.8 0.8 0 0 0 0-1.6z"/></svg>
        <span>1 (212) 555-0143</span>
      </li>
      <li>
        <svg class="contact-icon" viewBox="0 0 14 14" aria-hidden="true"><path d="M1 3h12v8H1zM1.6 3.6 7 8l5.4-4.4v0.9L7 9 1.6 4.5z" fill-rule="evenodd"/></svg>
        <span>dorian27@kiroharbour-mail.com</span>
      </li>
      <li>
        <svg class="contact-icon" viewBox="0 0 14 14" aria-hidden="true"><circle cx="7" cy="7" r="6"/><path d="M4 4.5c1.5-0.5 2 0.8 3 0.5s1 1.5 0 2-2 0.5-2 2 M8.5 9.5c1-0.5 2-0.3 2.5 0.5" stroke="var(--card-dark)" stroke-width="1.2" fill="none"/></svg>
        <span>www.kiroharbour.com</span>
      </li>
    </ul>
  </section>

  <section class="card card--back" aria-label="Business card back">
    <p class="wordmark wordmark--back">KIRO</p>
    <p class="back-url">www.kiroharbour.com</p>
  </section>
</main>
</body>
</html>
```